" é uma empresa produtora de polpas de frutas congeladas, sumos naturais, e gelados artesanais. comercialisamos os produtos para pessoas individuais , lojas, restaurants e eventos. funcianamento: a materia prima (fruta) chega a fabrica, e é processeda segungo um protocolo definido pelas normas de saude e higiene. posterioremente é embalado e armazenado. os pedidos dos clientes chegam por telefone ou whatsaap e nós procedemos de acordo. fazemos entregas ou o cliente vem a loja. em junho sera aberta a loja/restaurante/gelataria fisica. todos os products são processados por nós. usamos produtos de qualidade, sem corantes e sem conservantes artificiais. "

```html
<!DOCTYPE html>
<html lang="pt">
<head>
<meta charset="utf-8">
<title>Crachá Funcional – Frutos do Kwanza</title>
<link href="https://fonts.googleapis.com/css2?family=Raleway:wght@400;500;600;700&display=swap" rel="stylesheet">
<style>
  :root{
    --bg:#2b2b2d;
    --red-light:#9c1f22;
    --red-dark:#650c10;
    --gold:#f4b433;
    --gold-bar:#f2a900;
    --white:#ffffff;
    --paper-top:#ffffff;
    --paper-bottom:#e3e3e3;
    --field:#dcdcdc;
    --ink:#3a3a3a;
    --ink-soft:#6a6a6a;
    --slot:#1e1e1e;
    --brand-red:#b3191e;
  }
  *{box-sizing:border-box;margin:0;padding:0}
  html,body{width:1200px;height:1200px;overflow:hidden}
  body{background:var(--bg);font-family:"Raleway",sans-serif;position:relative}

  .badge{position:absolute;top:228px;width:512px;height:920px;border-radius:6px;overflow:hidden;box-shadow:0 10px 30px rgba(0,0,0,.45)}
  .badge--front{left:72px;background:linear-gradient(160deg,var(--red-light) 0%,#861619 50%,var(--red-dark) 100%)}
  .badge--back{left:614px;background:linear-gradient(180deg,var(--paper-top) 0%,#f1f1f1 55%,var(--paper-bottom) 100%)}

  .lanyard-slot{position:absolute;top:24px;left:50%;transform:translateX(-50%);width:124px;height:26px;border-radius:13px;background:var(--slot)}
  .accent-bar{position:absolute;bottom:0;left:91px;width:330px;height:18px;border-radius:9px 9px 0 0;background:var(--gold-bar)}

  /* Brand name with plain square */
  .brand{position:absolute;display:flex;align-items:center;justify-content:center;white-space:nowrap}
  .brand__mark{display:block;flex:0 0 auto}
  .brand__name{font-weight:700}

  /* Front */
  .brand--front{top:170px;left:0;right:0;gap:12px;color:var(--gold)}
  .brand--front .brand__mark{width:22px;height:22px;background:var(--gold)}
  .brand--front .brand__name{font-size:34px}
  .slogan{position:absolute;top:270px;left:0;right:0;text-align:center;font-weight:600;font-size:30px;color:var(--gold);letter-spacing:.5px}
  .photo{position:absolute;top:348px;left:142px;width:228px;height:294px;border-radius:14px;background:linear-gradient(180deg,#e9e6e2 0%,#c9a894 45%,#5a3325 100%)}
  .holder{position:absolute;top:652px;left:0;right:0;text-align:center;color:var(--white)}
  .holder__name{font-weight:700;font-size:33px}
  .holder__role{font-weight:500;font-size:24px;margin-top:6px}

  /* Back */
  .fields{position:absolute;top:161px;left:60px;width:392px}
  .field{position:relative;height:68px;border-radius:8px;background:var(--field);margin-bottom:34px}
  .field__label{position:absolute;top:6px;left:10px;font-size:10px;font-weight:500;color:var(--ink-soft)}
  .field__value{position:absolute;left:0;right:0;bottom:12px;text-align:center;font-size:24px;font-weight:600;color:var(--ink)}
  .notice{position:absolute;top:522px;left:40px;right:40px;text-align:center;font-size:19px;font-weight:700;color:var(--ink);line-height:1.25}
  .contacts{position:absolute;top:594px;left:52px;list-style:none}
  .contact{display:flex;align-items:flex-start;gap:12px;margin-bottom:14px;font-size:14px;font-weight:500;color:var(--ink);line-height:1.3}
  .contact svg{flex:0 0 26px;width:26px;height:26px}
  .brand--back{top:648px;left:318px;width:180px;gap:8px;color:var(--brand-red)}
  .brand--back .brand__mark{width:12px;height:12px;background:var(--brand-red)}
  .brand--back .brand__name{font-size:17px}
</style>
</head>
<body>
  <section class="badge badge--front">
    <span class="lanyard-slot"></span>
    <div class="brand brand--front">
      <span class="brand__mark"></span>
      <span class="brand__name">Frutos do Kwanza</span>
    </div>
    <div class="slogan">Sabor Saudável</div>
    <div class="photo" role="img" aria-label="Fotografia do funcionário"></div>
    <div class="holder">
      <div class="holder__name">Nome Completo</div>
      <div class="holder__role">Diretora Geral.</div>
    </div>
    <span class="accent-bar"></span>
  </section>

  <section class="badge badge--back">
    <span class="lanyard-slot"></span>
    <div class="fields">
      <div class="field"><span class="field__label">Nome do funcionário</span><span class="field__value">Nome Funcionário</span></div>
      <div class="field"><span class="field__label">Função</span><span class="field__value">Diretora Geral</span></div>
      <div class="field"><span class="field__label">Matrícula</span><span class="field__value">0000-00</span></div>
    </div>
    <p class="notice">É obrigatório o porte desta identidade<br>funcional em local visível</p>
    <ul class="contacts">
      <li class="contact">
        <svg viewBox="0 0 26 26"><circle cx="13" cy="13" r="12" fill="none" stroke="#3a3a3a" stroke-width="1.6"/><path d="M9 7.5l2.2-.3 1.2 3-1.4 1a7 7 0 003.4 3.4l1-1.4 3 1.2-.3 2.2c-5 .4-9.7-4.3-9.1-9.1z" fill="#3a3a3a"/></svg>
        <span>(11) 3400-7182<br>(11) 9870-2315</span>
      </li>
      <li class="contact">
        <svg viewBox="0 0 26 26"><circle cx="13" cy="13" r="12" fill="none" stroke="#3a3a3a" stroke-width="1.6"/><path d="M13 6a5 5 0 00-5 5c0 3.6 5 9 5 9s5-5.4 5-9a5 5 0 00-5-5zm0 7a2 2 0 110-4 2 2 0 010 4z" fill="#3a3a3a"/></svg>
        <span>Panificação Bom Gosto<br>Rua das Acácias Floridas, 118<br>São Paulo - SP - Cep: 04310-220</span>
      </li>
      <li class="contact">
        <svg viewBox="0 0 26 26"><circle cx="13" cy="13" r="12" fill="none" stroke="#3a3a3a" stroke-width="1.6"/><rect x="7" y="9" width="12" height="8.5" rx="1" fill="none" stroke="#3a3a3a" stroke-width="1.5"/><path d="M7.5 9.5l5.5 4.2 5.5-4.2" fill="none" stroke="#3a3a3a" stroke-width="1.5"/></svg>
        <span>contato@bomgostopolpas.com</span>
      </li>
    </ul>
    <div class="brand brand--back">
      <span class="brand__mark"></span>
      <span class="brand__name">Frutos do Kwanza</span>
    </div>
    <span class="accent-bar"></span>
  </section>
</body>
</html>
```